Lumen Ridge Agency Stationery
Lumen Ridge
Project: Lumen Ridge Agency Stationery
Lumen Ridge Agency Stationery - Advertising
Creative Brief
Simple
Doris Jean Malloway
Vice President, Corporate Operations
482 Fenwick Ave. Seattle, WA 98112
info@lumenridgeco.example
dorisjean@lumenridgeco.example
www.lumenridgeco.example
Front should have black background with LR circle only (no text). Would love to see the red circle and red plus raised to give them a 3-D look. You can do a standard rectangle business card or change it up and make it a circle.
Back should also be black background with white font. Occasionally you can use a red font if it looks cool to distinguish individual fields. Around the border of the card should be the company information (Address field, phone number (toll-free field), email (fax field), and website. Inside the center should be the person's name, title, direct line (phone field) and email. You can put the logo in the center again if it looks like to have that on the left and contact info on right, but it is not necessary to use the logo again. You can also try using icons with the text fields, but if it looks too busy, then don't worry about it. Thanks!

```html
<!DOCTYPE html>
<html lang="en">
<head>
<meta charset="utf-8">
<title>Lumen Ridge Agency Stationery</title>
<link href="https://fonts.googleapis.com/css2?family=Open+Sans:wght@400;600&display=swap" rel="stylesheet">
<style>
  :root{
    --backdrop:#ececec;
    --paper:#ffffff;
    --ink:#0d0d0d;
    --brand-red:#d41f26;
    --watermark:#f3c9cb;
    --muted:#7a7a7a;
  }
  *{margin:0;padding:0;box-sizing:border-box}
  html,body{width:1200px;height:936px;overflow:hidden}
  body{background:var(--backdrop);font-family:"Open Sans",Arial,sans-serif;position:relative}
  .piece{position:absolute;background:var(--paper);box-shadow:0 2px 6px rgba(0,0,0,.18);overflow:hidden}
  .piece svg.band{position:absolute;left:0;top:0;display:block}
  .mark{display:flex;align-items:center;gap:8px;position:absolute}
  .mark-dot{border-radius:50%;background:var(--brand-red);flex:none}
  .mark-name{font-weight:400;white-space:nowrap}

  .letterhead{left:190px;top:38px;width:392px;height:493px}
  .letterhead .mark{left:14px;top:12px}
  .letterhead .mark-dot{width:26px;height:26px}
  .letterhead .mark-name{color:#fff;font-size:13px}
  .contact-lines{position:absolute;right:14px;top:8px;color:#fff;font-size:5.5px;line-height:8px;text-align:left}
  .watermark{position:absolute;left:0;right:0;top:196px;text-align:center;color:var(--watermark);font-size:48px;font-weight:400}

  .folder{left:633px;top:38px;width:392px;height:582px;background:var(--ink)}
  .folder .mark{left:0;right:0;top:220px;flex-direction:column;gap:10px}
  .folder .mark-dot{width:86px;height:86px;border:3px solid #fff}
  .folder .mark-name{color:#fff;font-size:22px}
  .folder-web{position:absolute;left:0;right:0;bottom:14px;text-align:center;color:#fff;font-size:8px;letter-spacing:1px}

  .card-front{left:46px;top:658px;width:194px;height:101px;background:var(--ink)}
  .card-front .mark{left:10px;top:10px;flex-direction:column;gap:4px;width:60px}
  .card-front .mark-dot{width:26px;height:26px}
  .card-front .mark-name{color:#fff;font-size:7px}
  .card-person{position:absolute;left:80px;top:12px;width:106px;color:#fff;font-size:5.5px;line-height:8px;white-space:nowrap}
  .card-person .name{color:var(--brand-red);font-weight:600;font-size:6.5px}

  .card-back{left:46px;top:779px;width:194px;height:107px;background:var(--ink)}
  .card-back .initials{position:absolute;left:0;right:0;top:32px;text-align:center;color:#fff;font-size:28px;font-weight:400}
  .card-back .web{position:absolute;left:0;right:0;bottom:12px;text-align:center;color:#fff;font-size:6px;letter-spacing:.5px}

  .envelope{left:266px;top:670px;width:430px;height:210px}
  .envelope .mark{left:16px;top:14px}
  .envelope .mark-dot{width:28px;height:28px}
  .envelope .mark-name{color:#fff;font-size:14px}
  .envelope .address{position:absolute;left:52px;top:44px;color:#fff;font-size:5.5px}

  .envelope-back{left:734px;top:670px;width:430px;height:210px}
  .envelope-back .flap-web{position:absolute;left:0;right:0;top:28px;text-align:center;color:#fff;font-size:8px;letter-spacing:1.5px}
</style>
</head>
<body>

<section class="piece letterhead" aria-label="Letterhead">
  <svg class="band" width="392" height="70" viewBox="0 0 392 70">
    <path d="M0 0H392V34C300 60 200 30 120 44C70 52 30 58 0 50Z" fill="var(--ink)"/>
    <path d="M0 50C30 58 70 52 120 44C200 30 300 60 392 34V44C300 66 210 40 130 52C80 60 30 66 0 60Z" fill="var(--brand-red)"/>
  </svg>
  <div class="mark"><span class="mark-dot"></span><span class="mark-name">Lumen Ridge</span></div>
  <div class="contact-lines">
    482 Fenwick Ave. Seattle, WA 98112<br>
    Tel (206) 555-0148<br>
    info@lumenridgeco.example<br>
    www.lumenridgeco.example
  </div>
  <div class="watermark">LR</div>
</section>

<section class="piece folder" aria-label="Presentation folder">
  <svg class="band" width="392" height="582" viewBox="0 0 392 582">
    <path d="M0 500C120 540 260 470 392 486V530C270 510 140 560 0 548Z" fill="var(--paper)"/>
    <path d="M0 548C140 560 270 510 392 530V582H0Z" fill="var(--brand-red)"/>
  </svg>
  <div class="mark"><span class="mark-dot"></span><span class="mark-name">Lumen Ridge</span></div>
  <div class="folder-web">www.lumenridgeco.example</div>
</section>

<section class="piece card-front" aria-label="Business card front">
  <svg class="band" width="194" height="101" viewBox="0 0 194 101">
    <path d="M0 80C60 92 130 70 194 78V101H0Z" fill="var(--brand-red)"/>
  </svg>
  <div class="mark"><span class="mark-dot"></span><span class="mark-name">Lumen Ridge</span></div>
  <div class="card-person">
    <div class="name">Doris Jean Malloway</div>
    <div>Vice President, Corporate Operations</div>
    <div>482 Fenwick Ave. Seattle, WA 98112</div>
    <div>dorisjean@lumenridgeco.example</div>
    <div>www.lumenridgeco.example</div>
  </div>
</section>

<section class="piece card-back" aria-label="Business card back">
  <div class="initials">LR</div>
  <div class="web">www.lumenridgeco.example</div>
</section>

<section class="piece envelope" aria-label="Envelope front">
  <svg class="band" width="430" height="80" viewBox="0 0 430 80">
    <path d="M0 0H430V38C330 66 220 34 130 50C80 58 30 64 0 56Z" fill="var(--ink)"/>
    <path d="M0 56C30 64 80 58 130 50C220 34 330 66 430 38V48C330 74 230 44 140 58C90 66 35 72 0 66Z" fill="var(--brand-red)"/>
  </svg>
  <div class="mark"><span class="mark-dot"></span><span class="mark-name">Lumen Ridge</span></div>
  <div class="address">482 Fenwick Ave. Seattle, WA 98112</div>
</section>

<section class="piece envelope-back" aria-label="Envelope back">
  <svg class="band" width="430" height="110" viewBox="0 0 430 110">
    <path d="M0 0H430V60C320 96 200 44 90 74C50 84 20 92 0 88Z" fill="var(--brand-red)"/>
    <path d="M0 88C20 92 50 84 90 74C200 44 320 96 430 60V66C320 102 200 52 95 80C55 90 22 98 0 94Z" fill="#f2f2f2"/>
  </svg>
  <div class="flap-web">www.lumenridgeco.example</div>
</section>

</body>
</html>
```